Modern Fun - Family Oriented - Presentation Folder Design

We need a modern and family fun presentation folder design for a swimming pool company.Images are provided, use your creative imagination to use which ever works, edit, crop as needed.Company is "Brightwave Pools" www.brightwavepools.ca visit website to get colours, look and feel of brandSize is 9" x 12" with inside pockets 4" both sides - templates attachedSource file must be in .AI format providing PSD also doesn't hurt.

Target Market(s)

35 to 52 Age Group - Mostly Families

Font styles to use
Sans Serif

Colors

Designer to choose colors to be used in the design.

```html
<!DOCTYPE html>
<html lang="en">
<head>
<meta charset="utf-8">
<title>Brightwave Pools – Presentation Folder</title>
<link rel="stylesheet" href="https://fonts.googleapis.com/css2?family=Open+Sans:wght@400;600;700&family=Oswald:wght@500&family=Ubuntu:ital,wght@1,700&display=swap">
<style>
:root{
  --stage:#b5b0b0;
  --sky:#5ccaec;
  --pocket:#2574c0;
  --flap:#1d5da3;
  --navy:#1a4f9c;
  --mist:#e4e5eb;
  --ink:#1b1b1b;
  --sun:#f5e600;
}
*{margin:0;padding:0;box-sizing:border-box}
html,body{width:1200px;height:988px;overflow:hidden;background:var(--stage)}
.folder{position:relative;width:1200px;height:988px;font-family:"Open Sans",sans-serif;color:var(--ink)}
.dieline{position:absolute;left:0;top:0}
.panel-inside{position:absolute;left:168px;top:47px;width:461px;height:619px;background:var(--sky)}
.panel-cover{position:absolute;left:629px;top:457px;width:462px;height:209px;background:var(--mist)}
.photo-main{position:absolute;left:502px;top:47px;width:589px;height:410px;
  background:linear-gradient(160deg,#8aa4b8 0%,#2f6f9c 30%,#2a86b8 55%,#1e5d86 80%,#3b6f8c 100%)}
.fold{position:absolute;left:629px;top:47px;width:1px;height:410px;background:rgba(255,255,255,.55)}
.photo-inset{position:absolute;left:655px;top:403px;width:215px;height:154px;background:#222;border-top:4px solid var(--sun);padding:4px 4px 5px 4px}
.photo-inset div{width:100%;height:100%;background:linear-gradient(135deg,#8fd8f0,#3fb4e2 45%,#e48cc4 70%,#52b8e6)}
.brand{position:absolute;left:895px;top:488px;width:150px;display:flex;align-items:center;gap:6px;font-weight:700;font-size:17px;color:var(--navy);line-height:1}
.brand span.dot{width:14px;height:14px;border-radius:50%;background:var(--navy);flex:none}
.url-band{position:absolute;left:1051px;top:374px;width:40px;height:188px;background:#0f5fb0;display:flex;align-items:center;justify-content:center}
.url-band p{transform:rotate(-90deg);white-space:nowrap;color:#fff;font-weight:700;font-size:14px}
.headline{position:absolute;left:629px;top:584px;width:462px;text-align:center;font-family:"Ubuntu",sans-serif;font-style:italic;font-weight:700;font-size:29px;color:var(--navy);letter-spacing:.5px}
.rule{position:absolute;left:640px;width:440px;height:1px;background:linear-gradient(90deg,transparent,#5a78b5 20%,#5a78b5 80%,transparent)}
.tagline{position:absolute;left:629px;top:629px;width:462px;text-align:center;font-family:"Oswald",sans-serif;font-weight:500;font-size:12.5px;color:var(--ink)}
.why{position:absolute;left:201px;top:139px;width:269px}
.why h2{font-size:13px;font-weight:700;margin-bottom:9px}
.why p{font-size:9.8px;line-height:13.8px;text-align:justify;margin-bottom:9px}
.contacts{position:absolute;left:201px;top:548px;list-style:none}
.contacts li{display:flex;align-items:center;gap:8px;font-size:12.5px;height:18px}
.contacts li:nth-child(2){margin-top:8px}
.contacts li:nth-child(3){margin-top:12px}
.contacts svg{width:12px;height:12px;flex:none}
.dots{position:absolute;left:190px;top:638px;width:414px;border-top:1px dotted #4b6d86}
</style>
</head>
<body>
<div class="folder">
  <svg class="dieline" width="1200" height="988" viewBox="0 0 1200 988">
    <polygon points="168,659 130,698 130,827 168,865" fill="var(--flap)"/>
    <polygon points="1091,659 1133,698 1133,827 1091,865" fill="var(--flap)"/>
    <polygon points="168,666 629,666 616,865 168,865" fill="var(--pocket)"/>
    <polygon points="631,666 1091,666 1091,865 642,865" fill="var(--pocket)"/>
  </svg>

  <section class="panel-inside"></section>
  <section class="panel-cover"></section>
  <div class="photo-main" role="img" aria-label="Photo of children playing in a backyard fiberglass pool with lounge chairs and pool noodles"></div>
  <div class="fold"></div>

  <div class="why">
    <h2>WHY US</h2>
    <p>We’re a Different Kind of Swimming Pool Company. Learn why we do what we do as installers of world-class fiberglass swimming pools: with our exclusive 3 day groundbreaking to installed pool promise! Fiberglass Swimming Pools in Toronto Fiberglass Swimming Pools in Vaughan.</p>
    <p>Your backyard oasis should NOT take months to complete... Let’s Create Some Memories!</p>
  </div>

  <ul class="contacts">
    <li><svg viewBox="0 0 12 12"><circle cx="6" cy="6" r="5.5" fill="#fff" stroke="#222"/><path d="M4 3.2l1 1.3-.6.7c.4.9 1.1 1.6 2 2l.7-.6 1.3 1-.5 1c-2.3-.2-4.2-2.1-4.4-4.4z" fill="#222"/></svg>905.555.0148</li>
    <li><svg viewBox="0 0 12 12"><circle cx="6" cy="6" r="5.3" fill="#fff" stroke="#222"/><ellipse cx="6" cy="6" rx="2.2" ry="5.3" fill="none" stroke="#222" stroke-width=".8"/><path d="M1 6h10M1.8 3.5h8.4M1.8 8.5h8.4" stroke="#222" stroke-width=".8"/></svg>www.brightwavepools.ca</li>
    <li><svg viewBox="0 0 12 12"><circle cx="6" cy="6" r="5.8" fill="#fff"/><path d="M6 1.8a2.8 2.8 0 0 0-2.8 2.8c0 2.1 2.8 5.6 2.8 5.6s2.8-3.5 2.8-5.6A2.8 2.8 0 0 0 6 1.8zm0 3.9a1.1 1.1 0 1 1 0-2.2 1.1 1.1 0 0 1 0 2.2z" fill="#222"/></svg>22-1180 Harbourview Rd. Unit 140 Vaughan, ON L4K 2P7</li>
  </ul>
  <div class="dots"></div>

  <div class="photo-inset"><div role="img" aria-label="Underwater photo of a child swimming with goggles"></div></div>
  <div class="brand"><span class="dot"></span>Brightwave Pools</div>
  <div class="url-band"><p>www.brightwavepools.ca</p></div>

  <h1 class="headline">HAVE A SPLASHING HOLIDAY!</h1>
  <div class="rule" style="top:625px"></div>
  <p class="tagline">WE HELP FAMILIES CREATE NEW LIFE MEMORIES WITHOUT ALL THE STRESS</p>
  <div class="rule" style="top:650px"></div>
</div>
</body>
</html>
```